PREMIUM AGENCY High End Business Card - A+++ Designers Wanted

** DO NOT ATTEMPT TO CONTACT ME THROUGH SEARCHING ON ZINTREL OR EMAILING ME THROUGH MY WEBSITE **

I need a fresh, contemporary business card designed using the logo attached (BRONSALK)

I have attached the font for BRONSALK

It must have a premium look and feel. The business card size must be STANDARD size.

You can submit either/both VERTICAL or HORIZONTAL designs.

FRONT: It must have the following sample information on

Paul Ardley
Director Operations
Mobile +61 452 118 906
Email paulardley@bronsalk.com
www.bronsalk.com

The REAR of the business card must have the words

CREATE INSPIRE TOMORROW

as part of the design, in the same font (NEXA) attached.

The words do not need to be in capitals, or on the same line, please design this as you see it best working.

ADDITIONAL INFORMATION
======================

The BRONSALK logo must be on the front of the card

I want Ultraviolet printing on the final design, to enhance either the NAME of the person OR the BRONSALK logo OR the words on the back of the card.

Target Market(s)

Agency, Advertising Agency, Creative, Designers

Industry/Entity Type

Media

Contact Information for Business Card

Design Agency, Contemporary, Premium look and feel, High Quality

Font styles to use
Serif
Sans Serif
Other font styles liked:
• ATTACHED TO PROJECT

Requirements
Must have
• BLACK & WHITE as the primary design, and if you feel there can be a highlighted colour, then this can be used.
• The Logo ICON attached is blue, this colour must not be changed.
• I have attached the partner brand BRONSALK MEDIA incase you need to manipulate the original files.
• ** DO NOT ATTEMPT TO CONTACT ME THROUGH SEARCHING ON ZINTREL OR EMAILING ME THROUGH MY WEBSITE **
Nice to have
• Must be Premium. I have attached some sample designs, that I like that would be a good inspiration for where this can be taken.
• My favourite design is is the KESTRAVUE2-BUSINESSCARD-TEMPLATE
Should not have
• No funny or silly standard / off the shelf designs

```html
<!DOCTYPE html>
<html lang="en">
<head>
<meta charset="UTF-8">
<title>Bronsalk Media – Business Card</title>
<link href="https://fonts.googleapis.com/css2?family=Montserrat:wght@300;400;600;700&display=swap" rel="stylesheet">
<style>
  :root {
    --backdrop: #d9d9d9;
    --sky-light: #93c8ef;
    --sky: #6aa6df;
    --ink: #000000;
    --paper: #ffffff;
    --icon-blue: #4f95d8;
  }
  * { margin: 0; padding: 0; box-sizing: border-box; }
  html, body {
    width: 1200px; height: 1000px; overflow: hidden;
    background: var(--backdrop);
    font-family: "Montserrat", sans-serif;
  }
  .stage {
    width: 1200px; height: 1000px;
    display: flex; flex-direction: column;
    align-items: center; justify-content: center; gap: 60px;
  }
  .card {
    position: relative;
    width: 700px; height: 400px;
    background: linear-gradient(135deg, var(--sky-light) 0%, var(--sky) 55%, var(--sky) 100%);
    overflow: hidden;
    box-shadow: 0 12px 30px rgba(0,0,0,0.18);
  }
  .card__shape { position: absolute; inset: 0; width: 100%; height: 100%; }
  .brand {
    position: absolute; top: 26px; left: 30px;
    display: flex; align-items: center; gap: 8px;
    font-size: 15px; font-weight: 600; letter-spacing: 1.5px;
    color: var(--paper);
  }
  .brand__dot {
    width: 10px; height: 10px; border-radius: 50%;
    background: var(--icon-blue);
  }
  .card--back .brand { color: var(--ink); }
  .holder__name {
    position: absolute; top: 66px; left: 28px;
    font-size: 82px; font-weight: 600; letter-spacing: -1px;
    color: var(--paper); line-height: 1;
  }
  .holder__role {
    position: absolute; top: 156px; left: 30px;
    font-size: 44px; font-weight: 300;
    color: var(--paper); line-height: 1;
  }
  .contact {
    position: absolute; left: 200px; top: 262px;
    list-style: none;
    font-size: 22px; font-weight: 400; color: var(--ink);
  }
  .contact__item { display: flex; align-items: center; gap: 12px; height: 34px; }
  .contact__icon { width: 16px; height: 16px; flex: none; }
  .tagline {
    position: absolute; top: 178px; left: 50px;
    font-size: 34px; font-weight: 400; letter-spacing: 3px;
    color: var(--paper); white-space: nowrap;
  }
</style>
</head>
<body>
<main class="stage">

  <section class="card card--front" aria-label="Card front">
    <svg class="card__shape" viewBox="0 0 700 400" aria-hidden="true">
      <path fill="var(--ink)" d="M0,0 H500 C470,80 440,140 380,170 C300,210 200,200 120,215 C60,225 20,250 0,275 Z"/>
    </svg>
    <div class="brand"><span class="brand__dot"></span>BRONSALK MEDIA</div>
    <h1 class="holder__name">Paul Ardley</h1>
    <p class="holder__role">Director Operations</p>
    <ul class="contact">
      <li class="contact__item">
        <svg class="contact__icon" viewBox="0 0 16 16"><rect x="4" y="1" width="8" height="14" rx="1.5" fill="none" stroke="var(--ink)" stroke-width="1.5"/><circle cx="8" cy="12.5" r="0.9" fill="var(--ink)"/></svg>
        +61 452 118 906
      </li>
      <li class="contact__item">
        <svg class="contact__icon" viewBox="0 0 16 16"><circle cx="8" cy="8" r="6.5" fill="none" stroke="var(--ink)" stroke-width="1.5"/><path d="M1.5 8 H14.5 M8 1.5 C5 5 5 11 8 14.5 M8 1.5 C11 5 11 11 8 14.5" fill="none" stroke="var(--ink)" stroke-width="1.2"/></svg>
        www.bronsalk.com
      </li>
      <li class="contact__item">
        <svg class="contact__icon" viewBox="0 0 16 16"><rect x="1" y="3" width="14" height="10" fill="none" stroke="var(--ink)" stroke-width="1.5"/><path d="M1 3 L8 9 L15 3" fill="none" stroke="var(--ink)" stroke-width="1.5"/></svg>
        paulardley@bronsalk.com
      </li>
    </ul>
  </section>

  <section class="card card--back" aria-label="Card back">
    <svg class="card__shape" viewBox="0 0 700 400" aria-hidden="true">
      <path fill="var(--ink)" d="M700,0 V400 H560 C600,350 560,300 480,260 C400,220 380,180 420,130 C450,90 480,60 560,40 C620,25 660,10 700,0 Z"/>
    </svg>
    <div class="brand"><span class="brand__dot"></span>BRONSALK MEDIA</div>
    <p class="tagline">CREATE INSPIRE TOMORROW</p>
  </section>

</main>
</body>
</html>
```